Verpackungsdesign für Wellness- und Saunaprodukte
Zielgruppe
Brisavo ist ein junges Start-Up, das sich auf Wellness- und Saunaprodukte spezialisiert hat. Unsere Zielgruppe besteht zu beinahe gleichen Teilen aus männlichen und weiblichen Personen zwischen 30 und 60 Jahren. Unsere Produkte befinden sich eher im mittel- bis höherpreisigen Segment, daher streben wir ein hochwertiges Design für unsere Verpackungen an. Unsere Produktpalette reicht von Mentholkristallen, Saunaaufgüssen, bis hin zu Textilien für den Wellnessbereich und soll dementsprechend Menschen ansprechen, die sich einen gewissen Luxus im Alltag auch gönnen.
Aufgabenstellung
Inspiriert von der skandinavischen Sauna Kultur, möchten wir Momente der Erholung und
Entspannung in den Alltag unserer Kunden bringen. Die Geschichte des Saunierens ist eng mit der skandinavischen Kultur verbunden und skandinavische Stilelemente sind zeitgemäß und sprechen ein breites Publikum an. Das Design muss auf Dosen/Tiegel , Karton Verpackungen und Flaschen verschiedener Größen adaptierbar sein (siehe Bild im Anhang).
40g Tiegel(transparent) Höhe 40mm Durchmesser 60mm (ohne Deckel Silber gebürstet)
100g Tiegel(transparent) Höhe 53mm Durchmesser 71mm (ohne Deckel Silber gebürstet)
200g Tiegel(transparent) Höhe 65mm Durchmesser 90mm (ohne Deckel Silber gebürstet)
Karton Verpackung 124,5x49x49mm
Karton Verpackung 100x100x100mm
Flaschenetikett 134x67mm (Braunglas, schwarzer Deckel)
Es soll ein passendes Keyvisual erstellt werden.
Im Anhang sieht man die Verpackungen, Dosen, Flaschen sowie unsere ersten Design Entwürfe (an diese Anordnung der Elemente kann sich der Designer orientieren ). Das Logo bleibt wie gegeben. Das Produkt für die Tiegel soll Mentholkristalle sein.

```html
<!DOCTYPE html>
<html lang="de">
<head>
<meta charset="utf-8">
<title>Brisavo – Verpackungsdesign</title>
<link rel="stylesheet" href="https://fonts.googleapis.com/css2?family=Montserrat:wght@300;400;500&display=swap">
<style>
  :root {
    --page: #ffffff;
    --paper: #f7f7f7;
    --paper-jar: #f1f1f1;
    --band-grey: #d6d7d5;
    --band-mint: #d5e2de;
    --band-rose: #f0d7d8;
    --pine: #3f7866;
    --rose: #c0605a;
    --ornament: #d9d9d9;
    --ornament-faint: #ececec;
    --ink: #2b2b2b;
    --ink-soft: #555555;
    --rule: #c8c8c8;
  }
  * { margin: 0; padding: 0; box-sizing: border-box; }
  html, body { width: 988px; height: 1200px; overflow: hidden; background: var(--page); }
  body { position: relative; font-family: "Montserrat", sans-serif; color: var(--ink); }

  .key-ornament {
    position: absolute; left: 125px; top: 128px; width: 166px; height: 166px;
    border-radius: 50%; background: var(--ornament-faint);
  }

  .label { position: absolute; overflow: hidden; background: var(--paper); }
  .label > * { position: absolute; }
  .band-top, .band-bottom { left: 0; right: 0; background: var(--band-grey); }
  .brand-block {
    background: var(--pine); color: #ffffff; display: flex; align-items: flex-end;
    justify-content: center; font-weight: 400; letter-spacing: 0.2px;
  }
  .brand-block::before {
    content: ""; position: absolute; left: 50%; border: 1px solid #ffffff;
    transform: translateX(-50%);
  }
  .ornament { border-radius: 50%; background: var(--ornament); }
  .product-name {
    left: 0; right: 0; text-align: center; font-weight: 300; color: var(--ink-soft);
    line-height: 1.25;
  }
  .divider { height: 1px; background: linear-gradient(90deg, transparent, var(--rule) 20%, var(--rule) 80%, transparent); }
  .variant { left: 0; right: 0; text-align: center; font-weight: 400; color: var(--ink-soft); }
  .use-tag {
    background: var(--pine); color: #ffffff; font-weight: 500; text-align: center;
    display: flex; align-items: center; justify-content: center; line-height: 1.3;
  }
  .col-heading { text-align: center; font-weight: 400; color: var(--ink-soft); }
  .col-text { text-align: justify; text-align-last: center; font-weight: 400; line-height: 1.3; }
  .col-text p + p { margin-top: 1.3em; }
  .amount { font-weight: 400; color: var(--ink); }

  /* Box front 124,5 x 49 mm */
  .box-front { left: 694px; top: 251px; width: 101px; height: 284px; }
  .box-front .band-top { top: 0; height: 20px; }
  .box-front .band-bottom { bottom: 0; height: 29px; }
  .box-front .brand-block { left: 22px; top: 0; width: 55px; height: 55px; font-size: 8px; padding-bottom: 10px; }
  .box-front .brand-block::before { top: 14px; width: 14px; height: 14px; }
  .box-front .ornament { left: 31px; top: 186px; width: 38px; height: 38px; }
  .box-front .product-name { top: 148px; font-size: 9px; letter-spacing: 2.4px; padding-left: 2px; }
  .box-front .divider { left: 22px; width: 56px; top: 184px; }
  .box-front .variant { top: 192px; font-size: 5.5px; letter-spacing: 1.3px; }
  .box-front .use-tag { left: 25px; width: 54px; bottom: 0; height: 28px; font-size: 5.5px; }
  .box-front .ornament { top: 86px; }

  /* Bottle label 134 x 67 mm */
  .bottle-label { left: 321px; top: 487px; width: 327px; height: 163px; }
  .bottle-label .band-top { top: 0; height: 11px; }
  .bottle-label .band-bottom { bottom: 0; height: 18px; background: var(--band-mint); }
  .bottle-label .brand-block { left: 140px; top: 0; width: 48px; height: 38px; font-size: 7px; padding-bottom: 5px; }
  .bottle-label .brand-block::before { top: 8px; width: 12px; height: 12px; }
  .bottle-label .ornament { left: 147px; top: 51px; width: 36px; height: 36px; }
  .bottle-label .product-name { top: 98px; font-size: 8.5px; letter-spacing: 2.2px; padding-left: 2px; }
  .bottle-label .divider { left: 140px; width: 48px; top: 128px; }
  .bottle-label .variant { top: 133px; font-size: 5px; letter-spacing: 1.2px; }
  .bottle-label .use-tag { left: 140px; width: 48px; bottom: 0; height: 18px; font-size: 4.4px; }
  .bottle-label .col-left { left: 17px; top: 33px; width: 77px; }
  .bottle-label .col-right { left: 235px; top: 33px; width: 77px; }
  .bottle-label .col-heading { font-size: 5px; letter-spacing: 1.1px; margin-bottom: 6px; }
  .bottle-label .col-text { font-size: 3.7px; }
  .bottle-label .col-text p + p { margin-top: 8px; }
  .bottle-label .amount { left: 40px; top: 119px; font-size: 9px; }

  /* Jar labels 40 g */
  .jar-label { top: 868px; width: 277px; height: 95px; background: var(--paper-jar); }
  .jar-sauna { left: 190px; }
  .jar-body { left: 513px; }
  .jar-label .band-top { top: 0; height: 8px; }
  .jar-label .band-bottom { bottom: 0; height: 14px; }
  .jar-label .brand-block { left: 125px; top: 0; width: 35px; height: 27px; font-size: 5px; padding-bottom: 3px; }
  .jar-label .brand-block::before { top: 5px; width: 9px; height: 9px; }
  .jar-label .ornament { left: 132px; top: 32px; width: 20px; height: 20px; }
  .jar-label .product-name { top: 56px; font-size: 6.2px; letter-spacing: 1.7px; padding-left: 1px; }
  .jar-label .divider { left: 126px; width: 25px; top: 74px; }
  .jar-label .variant { top: 64px; font-size: 3.8px; font-weight: 500; color: var(--ink); }
  .jar-label .use-tag { left: 116px; width: 52px; bottom: 0; height: 14px; font-size: 4px; }
  .jar-label .col-left { left: 18px; top: 20px; width: 62px; }
  .jar-label .col-right { left: 197px; top: 20px; width: 62px; }
  .jar-label .col-heading { font-size: 4px; letter-spacing: 0.9px; margin-bottom: 5px; }
  .jar-label .col-text { font-size: 3.2px; }
  .jar-label .col-text p + p { margin-top: 5px; }
  .jar-label .amount { left: 39px; top: 61px; font-size: 7.5px; }

  .jar-body .band-top, .jar-body .band-bottom { background: var(--band-rose); }
  .jar-body .brand-block, .jar-body .use-tag { background: var(--rose); }
  .jar-body .divider { top: 72px; }
</style>
</head>
<body>

<div class="key-ornament" role="img" aria-label="Skandinavisches Blüten- und Blattornament als Keyvisual"></div>

<section class="label box-front" aria-label="Kartonverpackung Vorderseite">
  <div class="band-top"></div>
  <div class="band-bottom"></div>
  <div class="brand-block">Brisavo</div>
  <div class="ornament" role="img" aria-label="Skandinavisches Ornament"></div>
  <h2 class="product-name">NORDISCHE<br>FICHTE</h2>
  <div class="divider"></div>
  <p class="variant">AUFGUSS</p>
  <p class="use-tag">FÜR<br>DIE SAUNA</p>
</section>

<section class="label bottle-label" aria-label="Flaschenetikett">
  <div class="band-top"></div>
  <div class="band-bottom"></div>
  <div class="col-left">
    <h3 class="col-heading">INHALTSSTOFFE</h3>
    <div class="col-text">
      <p>Lorem ipsum dolor sit amet, consectetuer adipiscing elit, sed diam nonummy nibh euismod tincidunt ut laoreet dolore magna aliquam erat volutpat. Ut wisi enim ad</p>
      <p>Lorem ipsum dolor sit amet, consectetuer adipiscing elit, sed diam nonummy nibh euismod</p>
    </div>
  </div>
  <p class="amount">250 ml</p>
  <div class="brand-block">Brisavo</div>
  <div class="ornament" role="img" aria-label="Skandinavisches Ornament"></div>
  <h2 class="product-name">NORDISCHE<br>FICHTE</h2>
  <div class="divider"></div>
  <p class="variant">AUFGUSS</p>
  <p class="use-tag">FÜR DIE SAUNA</p>
  <div class="col-right">
    <h3 class="col-heading">ANWENDUNG</h3>
    <div class="col-text">
      <p>Lorem ipsum dolor sit amet, consectetuer adipiscing elit, sed diam nonummy nibh euismod tincidunt ut laoreet dolore magna aliquam erat volutpat. Ut wisi enim ad</p>
      <p>Lorem ipsum dolor sit amet, consectetuer adipiscing elit, sed diam nonummy nibh euismod</p>
      <p>Lorem ipsum dolor sit amet, consectetuer adipiscing elit, sed diam nonummy nibh euismod</p>
    </div>
  </div>
</section>

<section class="label jar-label jar-sauna" aria-label="Tiegeletikett Mentholkristalle">
  <div class="band-top"></div>
  <div class="band-bottom"></div>
  <div class="col-left">
    <h3 class="col-heading">INHALTSSTOFFE</h3>
    <div class="col-text">
      <p>Lorem ipsum dolor sit amet, consectetuer adipiscing elit, sed diam nonummy nibh euismod tincidunt ut laoreet dolore magna aliquam erat volutpat. Ut wisi enim ad</p>
    </div>
  </div>
  <p class="amount">40 g</p>
  <div class="brand-block">Brisavo</div>
  <div class="ornament" role="img" aria-label="Skandinavisches Ornament"></div>
  <h2 class="product-name">MENTHOL<br>KRISTALLE</h2>
  <div class="divider"></div>
  <p class="use-tag">FÜR DIE SAUNA</p>
  <div class="col-right">
    <h3 class="col-heading">ANWENDUNG</h3>
    <div class="col-text">
      <p>Lorem ipsum dolor sit amet, consectetuer adipiscing elit, sed diam nonummy nibh euismod tincidunt ut laoreet dolore magna aliquam erat volutpat. Ut wisi enim ad</p>
      <p>Lorem ipsum dolor sit amet, consectetuer adipiscing elit, sed diam nonummy nibh</p>
    </div>
  </div>
</section>

<section class="label jar-label jar-body" aria-label="Tiegeletikett Granatapfel Meersalzpeeling">
  <div class="band-top"></div>
  <div class="band-bottom"></div>
  <div class="col-left">
    <h3 class="col-heading">INHALTSSTOFFE</h3>
    <div class="col-text">
      <p>Lorem ipsum dolor sit amet, consectetuer adipiscing elit, sed diam nonummy nibh euismod tincidunt ut laoreet dolore magna aliquam erat volutpat. Ut wisi enim ad</p>
    </div>
  </div>
  <p class="amount">40 g</p>
  <div class="brand-block">Brisavo</div>
  <div class="ornament" role="img" aria-label="Skandinavisches Ornament"></div>
  <h2 class="product-name" style="top:56px">GRANATAPFEL</h2>
  <p class="variant" style="top:66px">Meersalzpeeling</p>
  <div class="divider"></div>
  <p class="use-tag">FÜR DEN KÖRPER</p>
  <div class="col-right">
    <h3 class="col-heading">ANWENDUNG</h3>
    <div class="col-text">
      <p>Lorem ipsum dolor sit amet, consectetuer adipiscing elit, sed diam nonummy nibh euismod tincidunt ut laoreet dolore magna aliquam erat volutpat. Ut wisi enim ad</p>
      <p>Lorem ipsum dolor sit amet, consectetuer adipiscing elit, sed diam nonummy nibh</p>
    </div>
  </div>
</section>

</body>
</html>
```